Real Estate Biz Card

-Card Size: Standard
-Background: Dark grey or black. I am open to gradient or a textured background.
-Other Colors: I dont mind pops of color. Contrasty blue, lime green, red Etc. Feel free to get creative.
-Text color: be creative
-Font: I like modern styles. Something that works well with my KV718 logo. See attached
-I would like my logo (KV718) watermarked on the card. Either on one side or both.
-Front of Card: keep it simple. Head shot, name, Logo, Phone #
-Back: add the rest of the details. See list below.
-brokerages logo as well as the Domivest and Equal Housing Opportunity logos on the card
-Name: Tod Marwick
-Residential Real Estate
-Cell:
-Email:
-Site:
-Office Address:
-very small/fine print "Each office independently owned & operated

```html
<!DOCTYPE html>
<html lang="en">
<head>
<meta charset="utf-8">
<title>KV718 Business Card – Tod Marwick</title>
<link href="https://fonts.googleapis.com/css2?family=Open+Sans:wght@400;600;700&family=Saira:wght@700&display=swap" rel="stylesheet">
<style>
  :root {
    --bg: #3a322e;
    --card: #17181a;
    --card-edge: #222326;
    --blue: #2f7fc4;
    --text: #f2f2f2;
    --muted: #8a8c90;
    --badge: #d9d9d9;
    --photo-a: #d4d6d9;
    --photo-b: #6f8fb8;
  }
  * { margin: 0; padding: 0; box-sizing: border-box; }
  html, body { width: 1200px; height: 864px; overflow: hidden; }
  body {
    background: var(--bg);
    position: relative;
    font-family: "Open Sans", Arial, sans-serif;
    color: var(--text);
  }
  .card {
    position: absolute;
    width: 600px;
    height: 343px;
    background: linear-gradient(160deg, var(--card-edge), var(--card));
    border-radius: 4px;
    box-shadow: 0 12px 30px rgba(0,0,0,.45);
    overflow: hidden;
  }
  .card--front { left: 90px; top: 80px; }
  .card--back { left: 510px; top: 440px; }

  .brand-name {
    font-family: "Saira", "Arial Black", sans-serif;
    font-weight: 700;
    color: var(--blue);
    letter-spacing: 2px;
    line-height: 1;
  }
  .card--front .brand-name {
    position: absolute;
    left: 150px;
    top: 100px;
    font-size: 104px;
  }
  .affiliations {
    position: absolute;
    left: 40px;
    bottom: 50px;
    display: flex;
    align-items: center;
    gap: 10px;
  }
  .affiliation-badge {
    width: 24px;
    height: 24px;
    background: var(--badge);
    border-radius: 2px;
  }
  .brokerage-name {
    margin-left: 6px;
    font-size: 15px;
    font-weight: 600;
    color: var(--text);
  }

  .card--back .brand-name {
    position: absolute;
    left: 34px;
    top: 34px;
    font-size: 62px;
  }
  .contact {
    position: absolute;
    left: 36px;
    top: 120px;
    list-style: none;
    font-size: 15px;
    line-height: 22px;
  }
  .contact li { display: flex; align-items: center; gap: 7px; }
  .contact .address { padding-left: 0; }
  .contact svg { width: 13px; height: 13px; fill: var(--text); flex: none; }
  .fine-print {
    position: absolute;
    left: 36px;
    top: 290px;
    font-size: 9px;
    color: var(--text);
  }
  .headshot {
    position: absolute;
    right: 40px;
    top: 36px;
    width: 200px;
    height: 196px;
    border-radius: 12px;
    background: linear-gradient(180deg, var(--photo-a) 0%, var(--photo-a) 45%, var(--photo-b) 100%);
  }
  .agent {
    position: absolute;
    right: 40px;
    top: 244px;
    width: 200px;
    text-align: center;
  }
  .agent-name {
    font-size: 17px;
    font-weight: 700;
    color: var(--blue);
    text-transform: uppercase;
  }
  .agent-title {
    font-size: 18px;
    color: var(--muted);
    white-space: nowrap;
  }
</style>
</head>
<body>
  <section class="card card--front">
    <div class="brand-name">KV718</div>
    <div class="affiliations">
      <span class="affiliation-badge"></span>
      <span class="affiliation-badge"></span>
      <span class="brokerage-name">Harbor Point Realty</span>
    </div>
  </section>

  <section class="card card--back">
    <div class="brand-name">KV718</div>
    <ul class="contact">
      <li class="address">2140 Larkspur Court</li>
      <li class="address">Juneau, Alaska 99801</li>
      <li><svg viewBox="0 0 16 16"><path d="M3 1h3l1 4-2 1.5a9 9 0 0 0 4.5 4.5L11 9l4 1v3a2 2 0 0 1-2 2A12 12 0 0 1 1 3a2 2 0 0 1 2-2z"/></svg>555 210 4471</li>
      <li><svg viewBox="0 0 16 16"><path d="M4 0h8a1 1 0 0 1 1 1v14a1 1 0 0 1-1 1H4a1 1 0 0 1-1-1V1a1 1 0 0 1 1-1zm1 2v10h6V2z"/></svg>555 318 6042</li>
      <li><svg viewBox="0 0 16 16"><path d="M0 3h16v10H0zm1.5 1.5L8 9l6.5-4.5V4h-13z"/></svg>tod@kv718.com</li>
      <li><svg viewBox="0 0 16 16"><circle cx="8" cy="8" r="8"/></svg>www.kv718.com</li>
    </ul>
    <p class="fine-print">Each office independently owned &amp; operated</p>
    <div class="headshot" role="img" aria-label="Headshot photo of Tod Marwick"></div>
    <div class="agent">
      <div class="agent-name">Tod Marwick</div>
      <div class="agent-title">Residential Real Estate</div>
    </div>
  </section>
</body>
</html>
```